Innovative Freezer Label Design

Create a versatile and innovative freezer label design with universal appeal, suitable for different functionalities. The design should cater to a diverse audience, including those who freeze meals for meal prepping, batch cooking, and the restaurant industry. Our vision is a visually striking and distinctive design that embodies simplicity.

Example "our current labels feature essential details like "Contents" and "Date." We recognize these as crucial points of information. Currently, the challenge lies in creating various labels for different marketplaces, considering language barriers. A proposed solution involves the integration of universal icons to replace specific words, promoting practicality for international sales."

Kindly note that design concepts should not be restricted to our current product, brand guideline, logo, or the provided example.

Our goal is not only product differentiation but also increased sales through a blend of functionality and aesthetics.

The following are examples of freezer labels designs. Kindly do not restrict your designs to the examples. The designs must be universal (for language barrier purposes)

Examples:
https://www.tackvora.co.uk/pin/5827164039281736401/
https://www.tackvora.co.uk/pin/5827164039281736405/
https://www.tackvora.co.uk/pin/5827164039281736394/
https://www.tackvora.co.uk/pin/5827164039281736308/
https://www.tackvora.co.uk/pin/5827164039281797750/

Please reach out if you have any questions.

Thank you

```html
<!DOCTYPE html>
<html lang="en">
<head>
<meta charset="utf-8">
<title>Freezer Label – Content &amp; Date</title>
<link href="https://fonts.googleapis.com/css2?family=Poppins:wght@600&display=swap" rel="stylesheet">
<style>
  :root {
    --backdrop: #ececec;
    --label-edge: #3d6566;
    --frame-sage: #9ab5a6;
    --writing-field: #ffffff;
    --tab-teal: #1d4d52;
    --caption-sage: #8fb0a0;
    --icon-teal: #1f4f55;
  }
  html, body {
    margin: 0;
    padding: 0;
    width: 1018px;
    height: 1200px;
    overflow: hidden;
    background: var(--backdrop);
  }
  .freezer-label {
    position: absolute;
    left: 59px;
    top: 375px;
    width: 900px;
    height: 450px;
    filter: drop-shadow(0 8px 14px rgba(0,0,0,0.18));
  }
  .label-caption {
    font-family: "Poppins", sans-serif;
    font-weight: 600;
    fill: var(--caption-sage);
  }
</style>
</head>
<body>
  <svg class="freezer-label" viewBox="0 0 712 356" xmlns="http://www.w3.org/2000/svg" role="group" aria-label="Freezer label with content and date fields">
    <!-- label body -->
    <rect class="label-edge" x="0" y="0" width="712" height="356" fill="var(--label-edge)"/>
    <rect class="sage-frame" x="19" y="21" width="674" height="315" fill="var(--frame-sage)"/>
    <rect class="writing-field" x="25" y="27" width="662" height="303" fill="var(--writing-field)"/>

    <!-- content heading tab -->
    <path class="content-tab" d="M25 27 H290 V114 Q290 126 278 126 H25 Z" fill="var(--tab-teal)"/>

    <!-- clipboard + pencil icon -->
    <g class="content-icon" fill="none" stroke="var(--caption-sage)" stroke-width="2" stroke-linecap="round" stroke-linejoin="round">
      <rect x="58" y="58" width="32" height="42" rx="3"/>
      <rect x="68" y="53" width="12" height="8" rx="2"/>
      <line x1="64" y1="70" x2="76" y2="70"/>
      <line x1="64" y1="77" x2="74" y2="77"/>
      <line x1="64" y1="84" x2="70" y2="84"/>
      <path d="M82 68 q6 8 2 22"/>
      <path d="M52 108 L57 96 L76 77 L82 83 L63 102 Z" fill="var(--tab-teal)"/>
      <line x1="57" y1="96" x2="63" y2="102"/>
    </g>
    <text class="label-caption content-caption" x="109" y="96" font-size="36">Content:</text>

    <!-- date row -->
    <g class="calendar-icon" fill="none" stroke="var(--icon-teal)" stroke-width="2.4">
      <rect x="47" y="284" width="35" height="31" rx="3"/>
      <line x1="47" y1="293" x2="82" y2="293"/>
      <line x1="55" y1="280" x2="55" y2="287"/>
      <line x1="74" y1="280" x2="74" y2="287"/>
    </g>
    <g class="calendar-days" fill="var(--icon-teal)">
      <rect x="52" y="298" width="4" height="3"/><rect x="59" y="298" width="4" height="3"/><rect x="66" y="298" width="4" height="3"/><rect x="73" y="298" width="4" height="3"/>
      <rect x="52" y="304" width="4" height="3"/><rect x="59" y="304" width="4" height="3"/><rect x="66" y="304" width="4" height="3"/><rect x="73" y="304" width="4" height="3"/>
      <rect x="52" y="310" width="4" height="2"/><rect x="59" y="310" width="4" height="2"/><rect x="66" y="310" width="4" height="2"/>
    </g>
    <text class="label-caption date-caption" x="102" y="307" font-size="21">Date:</text>
    <text class="label-caption date-divider" x="266" y="308" font-size="28">/</text>
    <text class="label-caption date-divider" x="402" y="308" font-size="28">/</text>
  </svg>
</body>
</html>
```